SaaS Early tech startup business card design

Unique design for experience ecommerce platform company. the business cards will be used by executive members. conformance with color code is required.

```html
<!DOCTYPE html>
<html lang="en">
<head>
<meta charset="utf-8">
<title>velto business card</title>
<link href="https://fonts.googleapis.com/css2?family=Poppins:wght@400;500;700;800&display=swap" rel="stylesheet">
<style>
  :root{
    --bg:#1c1c1f;
    --navy:#24223a;
    --navy-deep:#1d1b30;
    --teal:#22bb9c;
    --teal-soft:#4cbfaa;
    --blue:#0a6a8a;
    --blue-mid:#1592ab;
    --white:#ffffff;
  }
  *{margin:0;padding:0;box-sizing:border-box}
  html,body{width:1200px;height:900px;overflow:hidden;background:var(--bg);font-family:"Poppins",sans-serif}
  .canvas{position:relative;width:1200px;height:900px}
  .card{position:absolute;width:640px;height:366px;border-radius:28px;overflow:hidden;background:var(--navy);box-shadow:0 14px 30px rgba(0,0,0,.45)}
  .card-front{left:60px;top:60px}
  .card-back{left:500px;top:476px}

  .brand-name{position:absolute;font-family:"Poppins",sans-serif;font-weight:800;color:var(--teal);letter-spacing:-2px;line-height:1}
  .card-front .brand-name{right:150px;top:26px;font-size:96px}
  .card-back .brand-name{right:40px;top:34px;font-size:104px}

  .decor-knot{position:absolute;right:18px;top:120px;width:200px;height:130px;border-radius:50%;
    background:radial-gradient(ellipse at center,rgba(34,187,156,.35),rgba(21,146,171,.15) 55%,rgba(36,34,58,0) 75%)}

  .stat{position:absolute;left:44px;top:146px;color:var(--white)}
  .stat-figure{font-size:64px;font-weight:500;color:var(--teal);line-height:1}
  .stat-copy{font-size:20px;line-height:1.25;margin-top:4px;font-weight:400}

  .front-band{position:absolute;left:0;right:0;bottom:0;height:18px;
    background:linear-gradient(90deg,var(--blue) 0 16%,#0f7f9d 16% 32%,var(--blue-mid) 32% 48%,#1a9fb0 48% 64%,var(--teal-soft) 64% 80%,var(--teal) 80% 100%)}

  .holder{position:absolute;left:40px;top:118px}
  .holder-name{font-size:30px;font-weight:700;color:var(--teal);line-height:1.1}
  .holder-role{font-size:19px;color:var(--white)}

  .wave{position:absolute;inset:0}

  .contact-list{position:absolute;left:60px;bottom:36px;list-style:none;color:var(--white);font-size:21px;line-height:1.45}
  .contact-list li{display:flex;align-items:center;gap:12px}
  .contact-icon{width:26px;height:26px;flex:none}

  .address{position:absolute;right:36px;top:236px;text-align:right;color:var(--white);font-size:19px;line-height:1.3}
</style>
</head>
<body>
<main class="canvas">

  <section class="card card-front">
    <div class="brand-name">velto</div>
    <div class="decor-knot" role="img" aria-label="Soft teal line-art ribbon decoration"></div>
    <div class="stat">
      <div class="stat-figure">63%</div>
      <p class="stat-copy">Of Consumer Value<br>Privacy Over Popularity<br>When Dealing With<br>Online Platfrom</p>
    </div>
    <div class="front-band"></div>
  </section>

  <section class="card card-back">
    <svg class="wave" viewBox="0 0 640 366" width="640" height="366" aria-hidden="true">
      <defs>
        <linearGradient id="stripes" x1="0" y1="0" x2="1" y2="0">
          <stop offset="0" stop-color="#0a6a8a"/><stop offset=".16" stop-color="#0a6a8a"/>
          <stop offset=".16" stop-color="#0f7f9d"/><stop offset=".32" stop-color="#0f7f9d"/>
          <stop offset=".32" stop-color="#1592ab"/><stop offset=".48" stop-color="#1592ab"/>
          <stop offset=".48" stop-color="#1a9fb0"/><stop offset=".62" stop-color="#1a9fb0"/>
          <stop offset=".62" stop-color="#4cbfaa"/><stop offset=".78" stop-color="#4cbfaa"/>
          <stop offset=".78" stop-color="#3dc1a6"/><stop offset=".9" stop-color="#3dc1a6"/>
          <stop offset=".9" stop-color="#22bb9c"/><stop offset="1" stop-color="#22bb9c"/>
        </linearGradient>
      </defs>
      <path d="M0,300 C70,200 200,186 330,176 C470,164 590,140 640,44 L640,366 L0,366 Z" fill="#ffffff"/>
      <path d="M0,316 C80,214 210,198 340,188 C480,176 600,156 640,66 L640,366 L0,366 Z" fill="url(#stripes)"/>
    </svg>

    <div class="brand-name">velto</div>

    <div class="holder">
      <div class="holder-name">Jonathan Smith</div>
      <div class="holder-role">Manager</div>
    </div>

    <p class="address">Your address, city<br>state, ZIP 0000</p>

    <ul class="contact-list">
      <li>
        <svg class="contact-icon" viewBox="0 0 26 26" aria-hidden="true"><rect width="26" height="26" rx="6" fill="#fff"/><path d="M8 6c1 0 2 2.5 2 3.2S8.6 10.6 9 11.5c.8 2 3 4.2 5 5 .9.4 1.6-1 2.3-1s3.2 1 3.2 2-1.5 2.5-2.8 2.5C11 20 6 15 6 8.8 6 7.5 7 6 8 6z" fill="#24223a"/></svg>
        <span>123-456-2100</span>
      </li>
      <li>
        <svg class="contact-icon" viewBox="0 0 26 26" aria-hidden="true"><rect width="26" height="26" rx="6" fill="#fff"/><rect x="5" y="8" width="16" height="11" rx="1" fill="none" stroke="#24223a" stroke-width="2"/><path d="M5 8l8 6 8-6" fill="none" stroke="#24223a" stroke-width="2"/></svg>
        <span>youremail@mailbox.com</span>
      </li>
      <li>
        <svg class="contact-icon" viewBox="0 0 26 26" aria-hidden="true"><rect width="26" height="26" rx="6" fill="#fff"/><circle cx="13" cy="13" r="7" fill="none" stroke="#24223a" stroke-width="2"/><path d="M6 13h14M13 6c-3 3.5-3 10.5 0 14M13 6c3 3.5 3 10.5 0 14" fill="none" stroke="#24223a" stroke-width="1.6"/></svg>
        <span>www.yourwebsite.com</span>
      </li>
    </ul>
  </section>

</main>
</body>
</html>
```